Copper Lattice of Brave Movers

Hi - I would like your help transforming my (terrible) drawing into a graphic that pops -using hex colors I'll give you - so that I can put it into stationary and on t-shirts or tote bags. My company, the Tundrel Institute, trains social change leaders (from the sectors in the periodic table) on how to lead large-scale change. I have this vision - the "periodic table" but these are the sectors that my clients work in. If you are having trouble reading my writing, I apologize. Our hex colors are: #114769, #76984C, #80B5CF (Seagull), #8F2C63 and Rangoon Black #191919. You don't need to use all of them, but it'd be good to be consistent with our overall branding. If you can't read my writing, I will send correct spelling. The "Tundrel" with the flowers on the bottom is for a separate design bid.

Target Market(s)

nonprofit, social entrepreneurs, philanthropy, leaders

Requirements
Must have
• clean, readable font. alignment to look like periodic table of elements. heart icon for love, cat face for cats.

```html
<!DOCTYPE html>
<html lang="en">
<head>
<meta charset="utf-8">
<title>Copper Lattice of Brave Movers</title>
<link rel="stylesheet" href="https://fonts.googleapis.com/css2?family=Lexend:wght@400;500&display=swap">
<style>
  :root {
    --navy: #114769;
    --moss: #76984C;
    --seagull: #80B5CF;
    --plum: #8F2C63;
    --orchid: #CD5CA3;
    --ink: #000000;
    --paper: #FFFFFF;
    --tile: 102.6px;
    --gap: 4.65px;
  }
  * { box-sizing: border-box; margin: 0; padding: 0; }
  html, body { width: 679px; height: 1200px; overflow: hidden; }
  body { position: relative; font-family: "Lexend", sans-serif; background: var(--paper); }

  .edition { position: absolute; left: 0; width: 679px; }
  .edition--light { top: 0; height: 599px; background: var(--paper); }
  .edition--dark { top: 599px; height: 601px; background: var(--ink); }

  .lattice {
    position: absolute; left: 19.6px; top: 30px;
    display: grid;
    grid-template-columns: repeat(6, var(--tile));
    grid-template-rows: repeat(5, var(--tile));
    column-gap: var(--gap);
    row-gap: var(--gap);
  }

  .element {
    position: relative;
    border-radius: 14px;
    color: var(--paper);
    text-align: center;
  }
  .element--seagull { background: var(--seagull); }
  .element--navy { background: var(--navy); }
  .element--moss { background: var(--moss); }
  .element--plum { background: var(--plum); }
  .element--orchid { background: var(--orchid); transform: translateY(7px); }

  .element__symbol {
    position: absolute; left: 0; right: 0; top: 2px; height: 56px;
    display: flex; align-items: flex-end; justify-content: center;
    font-weight: 500; font-size: 57px; line-height: 1; letter-spacing: -2px;
  }
  .element__rule {
    position: absolute; left: 16px; right: 16px; top: 59.5px;
    height: 1px; background: var(--paper);
  }
  .element__name {
    position: absolute; left: 0; right: 0; top: 61px; bottom: 2px;
    display: flex; align-items: center; justify-content: center;
    font-size: 14.6px; line-height: 16px; font-weight: 400;
  }
  .element__icon { display: block; }
  .element__icon--cat {
    width: 50px; height: 48px; margin-bottom: 2px;
    border-radius: 16px 16px 22px 22px;
    background: rgba(255,255,255,0.22);
  }

  .span-gap { grid-column: 2 / 6; }
</style>
</head>
<body>

<section class="edition edition--light">
  <div class="lattice">
    <div class="element element--seagull"><span class="element__symbol">Av</span><span class="element__rule"></span><span class="element__name">Anti-<br>violence</span></div>
    <div class="span-gap"></div>
    <div class="element element--plum"><span class="element__symbol">B</span><span class="element__rule"></span><span class="element__name">Belonging</span></div>

    <div class="element element--navy"><span class="element__symbol">Ec</span><span class="element__rule"></span><span class="element__name">Early<br>Childhood</span></div>
    <div class="element element--moss"><span class="element__symbol">Cc</span><span class="element__rule"></span><span class="element__name">Climate<br>Change</span></div>
    <div class="element element--seagull"><span class="element__symbol">Ej</span><span class="element__rule"></span><span class="element__name">Envisioning<br>Justice</span></div>
    <div class="element element--seagull"><span class="element__symbol">Hs</span><span class="element__rule"></span><span class="element__name">Human<br>Sources</span></div>
    <div class="element element--seagull"><span class="element__symbol">Hc</span><span class="element__rule"></span><span class="element__name">Health<br>Care</span></div>
    <div class="element element--plum"><span class="element__symbol">H</span><span class="element__rule"></span><span class="element__name">Housing</span></div>

    <div class="element element--navy"><span class="element__symbol">Ed</span><span class="element__rule"></span><span class="element__name">Education</span></div>
    <div class="element element--moss"><span class="element__symbol">As</span><span class="element__rule"></span><span class="element__name">Atth<br>School</span></div>
    <div class="element element--moss"><span class="element__symbol">Sj</span><span class="element__rule"></span><span class="element__name">Social<br>Justice</span></div>
    <div class="element element--seagull"><span class="element__symbol">Cr</span><span class="element__rule"></span><span class="element__name">Civil<br>Rights</span></div>
    <div class="element element--seagull"><span class="element__symbol">He</span><span class="element__rule"></span><span class="element__name">Health<br>Equity</span></div>
    <div class="element element--plum"><span class="element__symbol">J</span><span class="element__rule"></span><span class="element__name">Jobs</span></div>

    <div class="element element--navy"><span class="element__symbol">Aw</span><span class="element__rule"></span><span class="element__name">Animal<br>Welfare</span></div>
    <div class="element element--moss"><span class="element__symbol"><span class="element__icon element__icon--cat" role="img" aria-label="Cat face icon"></span></span><span class="element__rule"></span><span class="element__name">Cats</span></div>
    <div class="element element--moss"><span class="element__symbol">Rj</span><span class="element__rule"></span><span class="element__name">Racial<br>Justice</span></div>
    <div class="element element--moss"><span class="element__symbol">Ir</span><span class="element__rule"></span><span class="element__name">Immign<br>Rights</span></div>
    <div class="element element--seagull"><span class="element__symbol">Bh</span><span class="element__rule"></span><span class="element__name">Behavioral<br>Health</span></div>
    <div class="element element--plum"><span class="element__symbol">Ig</span><span class="element__rule"></span><span class="element__name">Inter-<br>generational</span></div>

    <div></div>
    <div class="element element--orchid"><span class="element__symbol"><svg class="element__icon" width="52" height="50" viewBox="0 0 52 50" role="img" aria-label="Heart"><path d="M26 46 C12 36 4 28 4 17 C4 9 10 4 16 4 C21 4 24 7 26 10 C28 7 31 4 36 4 C42 4 48 9 48 17 C48 28 40 36 26 46 Z" fill="none" stroke="#fff" stroke-width="4" stroke-linejoin="round"/></svg></span><span class="element__rule"></span><span class="element__name">Love</span></div>
    <div class="element element--orchid"><span class="element__symbol">A</span><span class="element__rule"></span><span class="element__name">Authenticity</span></div>
    <div class="element element--orchid"><span class="element__symbol">H</span><span class="element__rule"></span><span class="element__name">Humility</span></div>
    <div class="element element--orchid"><span class="element__symbol">Au</span><span class="element__rule"></span><span class="element__name">Audacity</span></div>
    <div class="element element--orchid"><span class="element__symbol">J</span><span class="element__rule"></span><span class="element__name">Justice</span></div>
  </div>
</section>

<section class="edition edition--dark">
  <div class="lattice">
    <div class="element element--seagull"><span class="element__symbol">Av</span><span class="element__rule"></span><span class="element__name">Anti-<br>violence</span></div>
    <div class="span-gap"></div>
    <div class="element element--plum"><span class="element__symbol">B</span><span class="element__rule"></span><span class="element__name">Belonging</span></div>

    <div class="element element--navy"><span class="element__symbol">Ec</span><span class="element__rule"></span><span class="element__name">Early<br>Childhood</span></div>
    <div class="element element--moss"><span class="element__symbol">Cc</span><span class="element__rule"></span><span class="element__name">Climate<br>Change</span></div>
    <div class="element element--seagull"><span class="element__symbol">Ej</span><span class="element__rule"></span><span class="element__name">Envisioning<br>Justice</span></div>
    <div class="element element--seagull"><span class="element__symbol">Hs</span><span class="element__rule"></span><span class="element__name">Human<br>Sources</span></div>
    <div class="element element--seagull"><span class="element__symbol">Hc</span><span class="element__rule"></span><span class="element__name">Health<br>Care</span></div>
    <div class="element element--plum"><span class="element__symbol">H</span><span class="element__rule"></span><span class="element__name">Housing</span></div>

    <div class="element element--navy"><span class="element__symbol">Ed</span><span class="element__rule"></span><span class="element__name">Education</span></div>
    <div class="element element--moss"><span class="element__symbol">As</span><span class="element__rule"></span><span class="element__name">Atth<br>School</span></div>
    <div class="element element--moss"><span class="element__symbol">Sj</span><span class="element__rule"></span><span class="element__name">Social<br>Justice</span></div>
    <div class="element element--seagull"><span class="element__symbol">Cr</span><span class="element__rule"></span><span class="element__name">Civil<br>Rights</span></div>
    <div class="element element--seagull"><span class="element__symbol">He</span><span class="element__rule"></span><span class="element__name">Health<br>Equity</span></div>
    <div class="element element--plum"><span class="element__symbol">J</span><span class="element__rule"></span><span class="element__name">Jobs</span></div>

    <div class="element element--navy"><span class="element__symbol">Aw</span><span class="element__rule"></span><span class="element__name">Animal<br>Welfare</span></div>
    <div class="element element--moss"><span class="element__symbol"><span class="element__icon element__icon--cat" role="img" aria-label="Cat face icon"></span></span><span class="element__rule"></span><span class="element__name">Cats</span></div>
    <div class="element element--moss"><span class="element__symbol">Rj</span><span class="element__rule"></span><span class="element__name">Racial<br>Justice</span></div>
    <div class="element element--moss"><span class="element__symbol">Ir</span><span class="element__rule"></span><span class="element__name">Immign<br>Rights</span></div>
    <div class="element element--seagull"><span class="element__symbol">Bh</span><span class="element__rule"></span><span class="element__name">Behavioral<br>Health</span></div>
    <div class="element element--plum"><span class="element__symbol">Ig</span><span class="element__rule"></span><span class="element__name">Inter-<br>generational</span></div>

    <div></div>
    <div class="element element--orchid"><span class="element__symbol"><svg class="element__icon" width="52" height="50" viewBox="0 0 52 50" role="img" aria-label="Heart"><path d="M26 46 C12 36 4 28 4 17 C4 9 10 4 16 4 C21 4 24 7 26 10 C28 7 31 4 36 4 C42 4 48 9 48 17 C48 28 40 36 26 46 Z" fill="none" stroke="#fff" stroke-width="4" stroke-linejoin="round"/></svg></span><span class="element__rule"></span><span class="element__name">Love</span></div>
    <div class="element element--orchid"><span class="element__symbol">A</span><span class="element__rule"></span><span class="element__name">Authenticity</span></div>
    <div class="element element--orchid"><span class="element__symbol">H</span><span class="element__rule"></span><span class="element__name">Humility</span></div>
    <div class="element element--orchid"><span class="element__symbol">Au</span><span class="element__rule"></span><span class="element__name">Audacity</span></div>
    <div class="element element--orchid"><span class="element__symbol">J</span><span class="element__rule"></span><span class="element__name">Justice</span></div>
  </div>
</section>

</body>
</html>
```